Design cigar box art

design cigar box label similar to sample using Rodrigo Valdemar logos, fonts and associated art. 3" wide by 12" long.

Colors
f37122
f9ba93

```html
<!DOCTYPE html>
<html lang="en">
<head>
<meta charset="utf-8">
<title>Sombra Lobo – Cigar Box Label</title>
<link rel="stylesheet" href="https://fonts.googleapis.com/css2?family=Cinzel:wght@400;600&family=Lato:wght@400&family=Marcellus&family=Oswald:wght@500&display=swap">
<style>
  :root {
    --stage: #e9e4df;
    --label-black: #121212;
    --label-charcoal: #242424;
    --gold: #f2b01e;
    --amber: #f9ba93;
    --flame: #f37122;
    --ember: #c9321b;
    --sun: #ffd60a;
    --white: #ffffff;
    --smoke: #8a8a8a;
  }
  * { margin: 0; padding: 0; box-sizing: border-box; }
  html, body { width: 1200px; height: 900px; overflow: hidden; }
  body { background: var(--stage); position: relative; }
  .box-label {
    position: absolute;
    left: 495px; top: 30px;
    width: 210px; height: 840px;
    box-shadow: 0 10px 30px rgba(0,0,0,.25);
  }
  .box-label svg { display: block; width: 100%; height: 100%; }
  .maker-name { font-family: "Cinzel", serif; font-weight: 600; fill: var(--gold); letter-spacing: 1px; }
  .kicker { font-family: "Lato", sans-serif; fill: var(--white); }
  .product-name { font-family: "Marcellus", serif; }
  .product-sub { font-family: "Oswald", sans-serif; font-weight: 500; fill: var(--white); letter-spacing: 1px; }
  .tagline { font-family: "Cinzel", serif; font-weight: 400; fill: var(--gold); }
</style>
</head>
<body>
  <div class="box-label">
    <svg viewBox="0 0 182 732" xmlns="http://www.w3.org/2000/svg">
      <defs>
        <linearGradient id="label-bg" x1="0" y1="0" x2="0" y2="1">
          <stop offset="0" stop-color="var(--label-charcoal)"/>
          <stop offset=".5" stop-color="var(--label-black)"/>
          <stop offset="1" stop-color="var(--label-charcoal)"/>
        </linearGradient>
        <linearGradient id="name-fill" x1="0" y1="0" x2="1" y2="1">
          <stop offset="0" stop-color="var(--sun)"/>
          <stop offset=".5" stop-color="var(--flame)"/>
          <stop offset="1" stop-color="var(--ember)"/>
        </linearGradient>
        <radialGradient id="eye-fill">
          <stop offset="0" stop-color="#f6a21c"/>
          <stop offset=".35" stop-color="#b45a10"/>
          <stop offset=".6" stop-color="#2b2b2b"/>
          <stop offset="1" stop-color="#121212" stop-opacity="0"/>
        </radialGradient>
        <radialGradient id="smoke-fill">
          <stop offset="0" stop-color="var(--smoke)" stop-opacity=".45"/>
          <stop offset="1" stop-color="var(--smoke)" stop-opacity="0"/>
        </radialGradient>
        <linearGradient id="foot-fill" x1="0" y1="0" x2="0" y2="1">
          <stop offset="0" stop-color="var(--sun)"/>
          <stop offset=".55" stop-color="#f8a116"/>
          <stop offset="1" stop-color="var(--flame)"/>
        </linearGradient>
      </defs>

      <rect class="label-ground" width="182" height="732" fill="url(#label-bg)"/>

      <g class="maker-mark">
        <rect x="0" y="12" width="182" height="70" fill="#1a1a1a"/>
        <line x1="0" y1="12" x2="182" y2="12" stroke="var(--gold)" stroke-width="1.5"/>
        <line x1="0" y1="82" x2="182" y2="82" stroke="var(--gold)" stroke-width="1.5"/>
        <circle cx="91" cy="38" r="13" fill="var(--ember)"/>
        <text class="maker-name" x="91" y="70" font-size="9.5" text-anchor="middle">RODRIGO VALDEMAR</text>
      </g>

      <text class="kicker" x="167" y="127" font-size="14" text-anchor="end">Beware of the</text>
      <text class="product-name" x="88" y="160" font-size="40" text-anchor="middle" fill="url(#name-fill)">Sombra</text>
      <text class="product-sub" x="91" y="207" font-size="30" text-anchor="middle">LOBO</text>

      <ellipse class="eye-art" cx="97" cy="292" rx="58" ry="48" fill="url(#eye-fill)" role="img" aria-label="Close-up of a glowing amber creature eye in darkness"/>

      <g class="tagline" font-size="13.5" text-anchor="middle">
        <text x="90" y="383">IT WILL LEAVE</text>
        <text x="90" y="400">WITH YOUR</text>
        <text x="90" y="417">HEART</text>
        <text x="90" y="447">BUT YOU WILL</text>
        <text x="90" y="464">NEVER FEEL THE</text>
        <text x="90" y="481">BITE</text>
      </g>

      <ellipse class="smoke-art" cx="75" cy="585" rx="80" ry="85" fill="url(#smoke-fill)" role="img" aria-label="Wisps of rising cigar smoke"/>

      <g class="footer-band">
        <polygon points="0,656 91,617 182,656 182,732 0,732" fill="var(--white)"/>
        <polygon points="0,666 91,628 182,666 182,732 0,732" fill="url(#foot-fill)"/>
      </g>
    </svg>
  </div>
</body>
</html>
```